Website Design

This is a Website design project for a Software Developer / Consulting Company called Quindlex.

I would like to have a place for : blogs, partners, products, solutions and whatever you recommend. It would be nice to have a slot for Case Studies and Video Training.

I like our Competitor's site www.vorantix.example
I DO NOT LIKE our competitor's MAIN Page: www.sulvendo.example.
Although Sulvendo does have a nice way of putting blog news and twitter. below their webpage.

There should be a place for us to change our Logo: i.e. Like MIRALOO. EVeryday miraloo changes its logo color.

thanks

Kelmor
Updates

Deisgns look good. However, I would like to see more deisgn options. Please be a little creative. thank you

Kelmor

Reason: We need to do some more modifications. We will be narrowing down the selections and working with Designers to get it to final stage.

Industry/Entity Type

It Company

```html
<!DOCTYPE html>
<html lang="en">
<head>
<meta charset="utf-8">
<title>Quindlex – Big Data Analytics</title>
<link href="https://fonts.googleapis.com/css2?family=Arimo:wght@400;700&display=swap" rel="stylesheet">
<style>
  :root{
    --orange:#f97a12;
    --hero:#fda35f;
    --hero-light:#fec08f;
    --ink:#1c1c1c;
    --text:#555;
    --muted:#8d8d8d;
    --band:#f2f2f2;
    --rule:#dcdcdc;
    --tab:#c4c4c4;
    --black:#050505;
    --white:#fff;
  }
  *{box-sizing:border-box;margin:0;padding:0}
  html,body{width:1160px;height:1200px;overflow:hidden}
  body{position:relative;background:var(--white);font-family:"Arimo",Arial,sans-serif;color:var(--text)}
  .abs{position:absolute}

  .top-strip{left:0;top:0;width:1160px;height:8px;background:var(--black)}

  .brand{left:174px;top:28px;display:flex;align-items:center;gap:10px}
  .brand-dot{width:40px;height:40px;border-radius:50%;background:var(--orange)}
  .brand-name{font-size:32px;font-weight:700;color:var(--ink);letter-spacing:-0.5px}

  .social{top:35px;display:flex;gap:16px;left:864px}
  .social span{width:24px;height:24px;border-radius:4px;background:#b9b9b9}
  .social span.hot{background:var(--orange)}

  .nav{left:0;top:89px;width:1160px;height:48px;background:var(--band);border-bottom:6px solid var(--rule)}
  .nav ul{list-style:none;position:absolute;left:224px;top:0;display:flex;height:48px}
  .nav li{font-size:13px;color:var(--text);line-height:48px;padding:0 9px;letter-spacing:.2px}
  .nav li.active{background:var(--tab);color:var(--ink);padding:0 10px}

  .hero{left:0;top:143px;width:1160px;height:324px;background:linear-gradient(180deg,var(--hero) 0%,#fea468 70%,#fdb07a 100%)}
  .hero-art{left:210px;top:30px;width:240px;height:250px;border-radius:8px;background:radial-gradient(ellipse at 45% 45%,var(--hero-light) 0%,rgba(254,192,143,0) 70%)}
  .hero-title{left:523px;top:116px;font-size:19px;color:var(--white);letter-spacing:.1px}
  .hero-sub{left:524px;top:148px;font-size:12.5px;color:var(--white)}
  .hero-lead{left:524px;top:164px;font-size:15.5px;color:var(--white)}
  .hero-btn{left:524px;top:193px;width:107px;height:23px;background:var(--white);color:var(--ink);font-size:12px;font-weight:700;text-align:center;line-height:23px}

  .section-title{left:201px;width:758px;height:24px;text-align:center}
  .section-title::before{content:"";position:absolute;left:0;right:0;top:12px;border-top:1px solid #ececec}
  .section-title h2{position:relative;display:inline-block;background:var(--white);padding:0 12px;font-size:21px;font-weight:400;color:var(--ink);letter-spacing:.5px}
  .section-title h2 b{font-weight:400;color:var(--orange)}

  .event{top:531px;width:243px}
  .event-photo{height:129px}
  .event h3{font-size:12px;font-weight:400;color:var(--ink);margin-top:10px;padding-bottom:9px;border-bottom:1px solid #e2e2e2}
  .event p{font-size:9px;line-height:13px;color:var(--muted);margin-top:9px}

  .solutions-box{left:201px;top:787px;width:758px;height:58px;background:var(--band);padding:17px 12px 0;font-size:9.5px;line-height:13px;color:#a3a3a3;text-align:center}

  .clients{left:213px;top:913px;width:736px;display:flex;justify-content:space-between;align-items:center}
  .clients span{font-size:17px;color:#6a6a6a}

  .footer{left:0;top:973px;width:1160px;height:182px;background:var(--band)}
  .col-rule{top:995px;width:1px;height:140px;background:#d6d6d6}
  .foot-h{font-size:16px;color:var(--ink);font-weight:400}
  .foot-p{font-size:9.5px;line-height:13px;color:var(--muted)}
  .more{font-size:10px;font-weight:700;color:var(--orange)}
  .blog-tile{left:481px;top:1047px;width:62px;height:42px;background:var(--orange);color:var(--white);font-size:15px;font-weight:700;text-align:center;line-height:42px}
  .field{left:791px;width:156px;height:21px;background:var(--white);border:1px solid #ddd;font-size:9px;color:#aaa;padding-left:6px;line-height:19px}
  .field-icon{left:762px}
  .submit{left:892px;top:1100px;width:53px;height:21px;background:var(--orange);color:var(--white);font-size:11px;font-weight:700;text-align:center;line-height:21px}

  .base{left:0;top:1155px;width:1160px;height:45px;background:var(--black);font-size:9px;color:var(--orange)}
  .base-links{left:177px;top:20px}
  .base-copy{right:172px;top:20px}
</style>
</head>
<body>
  <div class="abs top-strip"></div>

  <header>
    <div class="abs brand"><span class="brand-dot"></span><span class="brand-name">quindlex</span></div>
    <div class="abs social" aria-label="Social links"><span></span><span></span><span class="hot"></span></div>
  </header>

  <nav class="abs nav">
    <ul>
      <li class="active">HOME</li><li>PARTNERS</li><li>PRODUCTS</li><li>SOLUTIONS</li><li>CASE STUDIES</li><li>VIDEO TRAINING</li><li>COMPANY</li><li>BLOGS</li>
    </ul>
  </nav>

  <section class="abs hero">
    <div class="abs hero-art" role="img" aria-label="Wireframe hand reaching toward floating wireframe spheres over a grid"></div>
    <div class="abs hero-title">INDUSTRY THOUGHT LEADERS TALKING</div>
    <div class="abs hero-sub">BIG DATA ANALYTICS</div>
    <div class="abs hero-lead">FOR THE FACT - BASED ECONOMY</div>
    <div class="abs hero-btn">VIEW DETAILED</div>
  </section>

  <div class="abs section-title" style="top:499px"><h2><b>E</b>VENTS</h2></div>

  <article class="abs event" style="left:201px">
    <div class="event-photo" role="img" aria-label="Technician in cleanroom gear assembling hardware" style="background:linear-gradient(160deg,#6f8a86,#2f4d4a 60%,#1c2524)"></div>
    <h3>Data Integration</h3>
    <p>Get any data in with built-in connections to 50+ structured and unstructured data sources..</p>
  </article>
  <article class="abs event" style="left:459px">
    <div class="event-photo" role="img" aria-label="Engineer working at a lab bench full of equipment" style="background:linear-gradient(160deg,#c9cbc8,#6d6f6c 55%,#3a3b39)"></div>
    <h3>Data Analytics</h3>
    <p>240+ pre-built analytic functions with instant previews of the results</p>
  </article>
  <article class="abs event" style="left:716px">
    <div class="event-photo" role="img" aria-label="Close view of a dark laptop keyboard" style="background:linear-gradient(160deg,#5a5e63,#25282b 55%,#0e0f10)"></div>
    <h3>Data Visualization</h3>
    <p>Design, annotate and share custom data visualizations on any device</p>
  </article>

  <div class="abs section-title" style="top:753px"><h2><b>S</b>OLUTIONS</h2></div>
  <div class="abs solutions-box">The office data stored in the cloud, but because the server cannot accomplish real-time backup, once the failure occurs, will affect the normal business,Work division of labor cooperation way, each team members responsible for the work of a joint, once one or several computer fault, could lead to the entire work link cannot join</div>

  <div class="abs section-title" style="top:880px"><h2><b>C</b>ASE STUDIES</h2></div>
  <div class="abs clients">
    <span>Ferndale</span><span>Miraloo</span><span>Corvana</span><span>Talvet</span><span>Ostrane</span><span>Brelo</span><span>Nexavo</span><span>Pyrwell</span><span>Lumora</span>
  </div>

  <footer>
    <div class="abs footer"></div>
    <div class="abs col-rule" style="left:460px"></div>
    <div class="abs col-rule" style="left:740px"></div>

    <h4 class="abs foot-h" style="left:207px;top:999px">ABOUT US</h4>
    <p class="abs foot-p" style="left:207px;top:1025px;width:228px">Through many years of r&amp;d, has become a banner in the field of data recovery. Here, by the domestic first-class storage technology talent to form a powerful data recovery technology research and development center for us in the field of data recovery technology provides stable technical output protection.</p>
    <a class="abs more" style="left:207px;top:1122px">Read more...</a>

    <h4 class="abs foot-h" style="left:481px;top:999px">QUINDLEX BLOG</h4>
    <p class="abs foot-p" style="left:481px;top:1027px">Big Data Musings from quindlex CEO</p>
    <div class="abs blog-tile">BLOG</div>
    <p class="abs foot-p" style="left:551px;top:1043px;width:175px">Last week, over my first taste of a Brindlecreek Amber, I had the chance to talk to Dane Holloway</p>
    <p class="abs foot-p" style="left:484px;top:1095px;width:240px">about where he thinks big data will be in the next five to 10 years...</p>
    <a class="abs more" style="left:485px;top:1125px">Read more...</a>

    <h4 class="abs foot-h" style="left:759px;top:999px">EMAIL SIGNUP</h4>
    <svg class="abs field-icon" style="top:1035px" width="20" height="20" viewBox="0 0 20 20" aria-hidden="true"><circle cx="10" cy="6" r="4.5" fill="none" stroke="#f97a12" stroke-width="1.4"/><path d="M2 19c0-5 4-7.5 8-7.5s8 2.5 8 7.5z" fill="none" stroke="#f97a12" stroke-width="1.4"/></svg>
    <div class="abs field" style="top:1035px">Name</div>
    <svg class="abs field-icon" style="top:1069px" width="22" height="17" viewBox="0 0 22 17" aria-hidden="true"><rect x="1" y="1" width="20" height="15" fill="none" stroke="#f97a12" stroke-width="1.4"/><path d="M1 1l10 8 10-8M1 16l7-7M21 16l-7-7" fill="none" stroke="#f97a12" stroke-width="1.4"/></svg>
    <div class="abs field" style="top:1067px">Email ID</div>
    <div class="abs submit">SUBMIT</div>

    <div class="abs base">
      <div class="abs base-links">Home &nbsp;|&nbsp; Services &nbsp;|&nbsp; Blog &nbsp;|&nbsp; Contact Us</div>
      <div class="abs base-copy">© 2014 Quindlex, Inc. All rights reserved.</div>
    </div>
  </footer>
</body>
</html>
```